REDESIGN COUPLE PAGES FOR SURGE VIDEO ADS

PLEASE REDESIGN THIS PAGE FOR ME:
http://pagekitfinder.com/rk/milo/surge/pricing.html
I need it to be easy to read for the end user so the customer knows exactly what he will be getting. Make an emphasis on the subscription as the most popular item....and also the price per video format should be emphasized too.

Target Market(s)

B2B

Industry/Entity Type

Video Production

Number of Pages Required

3 page

Colors

Designer to choose colors to be used in the design.

Requirements
Must have
• PLEASE REDESIGN THIS PAGE FOR ME:
• http://pagekitfinder.com/rk/milo/surge/pricing.html
• I need it to be easy to read for the end user so the customer knows exactly what he will be getting. Make an emphasis on the subscription as the most popular item....and also the price per video format should be emphasized too.
Nice to have
Should not have

```html
<!DOCTYPE html>
<html lang="en">
<head>
<meta charset="utf-8">
<title>Premium Features Included in All Plans</title>
<link rel="stylesheet" href="https://fonts.googleapis.com/css2?family=Encode+Sans+Semi+Condensed:wght@700&family=Mulish:ital,wght@0,800;1,800&family=Questrial&display=swap">
<style>
  :root {
    --navy: #1b2d52;
    --ink: #3b3a3c;
    --ink-soft: #575659;
    --icon: #3a3839;
    --icon-light: #6a696b;
    --paper: #ffffff;
  }
  * { margin: 0; padding: 0; box-sizing: border-box; }
  html, body { width: 1200px; height: 694px; overflow: hidden; background: var(--paper); }
  .features { position: relative; width: 1200px; height: 694px; }
  .banner { position: absolute; left: 262px; top: 42px; width: 768px; height: 98px; }
  .banner svg { position: absolute; inset: 0; }
  .banner h1 {
    position: absolute; inset: 0; display: flex; align-items: center; justify-content: center;
    padding-right: 28px;
    font-family: "Encode Sans Semi Condensed", sans-serif; font-weight: 700;
    font-size: 28.5px; letter-spacing: 0.2px; color: var(--paper);
  }
  .icon { position: absolute; }
  .icon svg { display: block; width: 100%; height: 100%; }
  .feature { position: absolute; }
  .feature h3 {
    font-family: "Mulish", sans-serif; font-weight: 800; font-size: 19.5px;
    line-height: 25.5px; color: var(--ink); letter-spacing: 0.3px;
  }
  .feature p {
    font-family: "Questrial", sans-serif; font-size: 20px; line-height: 25.5px;
    color: var(--ink-soft); letter-spacing: 0.2px;
  }
  .feature p.em { font-style: italic; }
  .section-title {
    position: absolute; left: 0; width: 1188px; top: 520px; text-align: center;
    font-family: "Mulish", sans-serif; font-weight: 800; font-style: italic;
    font-size: 24px; color: var(--ink); letter-spacing: 0.6px;
  }
</style>
</head>
<body>
<main class="features">
  <svg width="0" height="0" style="position:absolute">
    <defs>
      <symbol id="projector" viewBox="0 0 192 162">
        <g fill="var(--icon)">
          <circle cx="36" cy="60" r="34"/>
          <circle cx="113" cy="40" r="39"/>
          <rect x="30" y="86" width="136" height="56" rx="8"/>
          <path d="M164 98 L192 84 L192 132 L164 118 Z"/>
          <rect x="82" y="142" width="30" height="10"/>
          <rect x="62" y="150" width="70" height="10" rx="3"/>
        </g>
        <g fill="none" stroke="var(--paper)" stroke-width="5">
          <circle cx="36" cy="60" r="25"/>
          <circle cx="113" cy="40" r="29"/>
          <path d="M36 35 V85 M11 60 H61 M18 42 L54 78 M54 42 L18 78"/>
          <path d="M113 11 V69 M84 40 H142 M92 19 L134 61 M134 19 L92 61"/>
        </g>
        <g fill="var(--icon)">
          <circle cx="36" cy="60" r="8"/>
          <circle cx="113" cy="40" r="9"/>
        </g>
      </symbol>
      <symbol id="note" viewBox="0 0 135 155">
        <g fill="var(--icon)">
          <ellipse cx="24" cy="132" rx="24" ry="22" transform="rotate(-20 24 132)"/>
          <ellipse cx="110" cy="104" rx="24" ry="22" transform="rotate(-20 110 104)"/>
          <rect x="38" y="36" width="11" height="98"/>
          <rect x="124" y="0" width="11" height="108"/>
          <path d="M38 30 C70 30 105 20 135 0 L135 30 C105 48 70 56 38 58 Z"/>
        </g>
      </symbol>
    </defs>
  </svg>

  <header class="banner">
    <svg viewBox="0 0 768 98" preserveAspectRatio="none" aria-hidden="true">
      <path fill="var(--navy)" d="M14 14 L120 8 L300 6 L520 4 L700 2 L740 0 L748 8 L762 10 L742 16 L768 22 L745 30 L760 40 L738 48 L756 58 L735 66 L752 74 L728 82 L700 88 L560 92 L400 94 L200 96 L40 94 L10 88 L14 76 L4 66 L10 54 L0 44 L8 32 L4 22 Z"/>
    </svg>
    <h1>PREMIUM FEATURES INCLUDED IN ALL PLANS</h1>
  </header>

  <!-- Row 1 -->
  <div class="icon" style="left:115px;top:170px;width:82px;height:87px">
    <svg viewBox="0 0 82 87" aria-hidden="true"><path fill="var(--icon)" d="M0 50 L10 47 L38 70 C48 40 62 18 82 0 C68 22 54 50 42 87 L36 87 Z"/></svg>
  </div>
  <div class="feature" style="left:200px;top:194px">
    <h3>Unlimited Revisions</h3>
    <p>Information Here</p>
  </div>

  <div class="icon" style="left:444px;top:182px;width:72px;height:75px">
    <svg viewBox="0 0 72 75" aria-hidden="true">
      <rect x="2" y="2" width="68" height="71" rx="5" fill="none" stroke="var(--icon)" stroke-width="4"/>
      <rect x="2" y="2" width="68" height="13" fill="var(--icon)"/>
      <rect x="2" y="60" width="68" height="13" fill="var(--icon)"/>
      <g fill="var(--paper)">
        <rect x="8" y="6" width="4" height="6"/><rect x="16" y="6" width="4" height="6"/><rect x="24" y="6" width="4" height="6"/><rect x="32" y="6" width="4" height="6"/><rect x="40" y="6" width="4" height="6"/><rect x="48" y="6" width="4" height="6"/><rect x="56" y="6" width="4" height="6"/>
        <rect x="8" y="63" width="4" height="6"/><rect x="16" y="63" width="4" height="6"/><rect x="24" y="63" width="4" height="6"/><rect x="32" y="63" width="4" height="6"/><rect x="40" y="63" width="4" height="6"/><rect x="48" y="63" width="4" height="6"/><rect x="56" y="63" width="4" height="6"/>
      </g>
    </svg>
  </div>
  <div class="feature" style="left:528px;top:194px">
    <h3>Large Square Video<br>Formating</h3>
    <p>Information Here</p>
  </div>

  <div class="icon" style="left:762px;top:184px;width:84px;height:73px">
    <svg viewBox="0 0 84 73" aria-hidden="true">
      <g fill="var(--icon-light)">
        <circle cx="15" cy="27" r="11"/><path d="M0 73 L3 44 C6 36 24 36 27 44 L30 73 Z"/>
        <circle cx="69" cy="27" r="11"/><path d="M54 73 L57 44 C60 36 78 36 81 44 L84 73 Z"/>
      </g>
      <g fill="var(--icon)">
        <circle cx="42" cy="14" r="14"/><path d="M22 73 L25 38 C29 27 55 27 59 38 L62 73 Z"/>
      </g>
    </svg>
  </div>
  <div class="feature" style="left:853px;top:194px">
    <h3>Personalized<br>Content</h3>
    <p class="em">Information Here</p>
  </div>

  <!-- Row 2 -->
  <div class="icon" style="left:91px;top:315px;width:102px;height:64px">
    <svg viewBox="0 0 102 64" aria-hidden="true">
      <ellipse cx="51" cy="32" rx="48" ry="29" fill="none" stroke="var(--icon)" stroke-width="5"/>
      <text x="51" y="41" text-anchor="middle" font-family="Mulish, sans-serif" font-weight="800" font-style="italic" font-size="26" fill="var(--icon)">Logo</text>
    </svg>
  </div>
  <div class="feature" style="left:200px;top:308px">
    <h3>Branding</h3>
    <p>Full Branding In<br>Video</p>
  </div>

  <div class="icon" style="left:442px;top:307px;width:71px;height:71px">
    <svg viewBox="0 0 71 71" aria-hidden="true">
      <circle cx="35.5" cy="35.5" r="32" fill="none" stroke="var(--icon)" stroke-width="6"/>
      <path d="M49 25 A17 17 0 1 0 49 46" fill="none" stroke="var(--icon)" stroke-width="8"/>
    </svg>
  </div>
  <div class="feature" style="left:528px;top:308px">
    <h3>Copyright</h3>
    <p>Full Copyright<br>Ownership</p>
  </div>

  <div class="icon" style="left:776px;top:307px;width:58px;height:72px">
    <svg viewBox="0 0 58 72" aria-hidden="true">
      <rect x="24" y="0" width="9" height="72" fill="var(--icon)"/>
      <path d="M50 18 C46 12 38 10 29 10 C14 10 8 17 8 24 C8 40 52 34 52 50 C52 58 44 62 29 62 C18 62 10 58 6 52" fill="none" stroke="var(--icon)" stroke-width="13"/>
    </svg>
  </div>
  <div class="feature" style="left:853px;top:308px">
    <h3>Reselling</h3>
    <p class="em">Full Reselling Rights</p>
  </div>

  <!-- Row 3 -->
  <div class="icon" style="left:86px;top:403px;width:107px;height:91px">
    <svg viewBox="0 0 192 162" aria-hidden="true"><use href="#projector"/></svg>
  </div>
  <div class="feature" style="left:200px;top:423px">
    <h3>Premium Video Clips</h3>
    <p>Information Here</p>
  </div>

  <div class="icon" style="left:434px;top:406px;width:76px;height:87px">
    <svg viewBox="0 0 135 155" aria-hidden="true"><use href="#note"/></svg>
  </div>
  <div class="feature" style="left:528px;top:423px">
    <h3>Fully Licensed Background Music</h3>
    <p>Information Here</p>
  </div>

  <h2 class="section-title">PERSONALIZED CONTENT</h2>

  <!-- Row 4 -->
  <div class="icon" style="left:99px;top:574px;width:85px;height:70px">
    <svg viewBox="0 0 85 70" aria-hidden="true">
      <path fill="var(--icon)" d="M6 8 H16 V3 H28 V8 H62 L66 3 H76 L79 8 C82 8 85 10 85 14 V64 C85 67 82 70 79 70 H6 C3 70 0 67 0 64 V14 C0 10 3 8 6 8 Z"/>
      <circle cx="43" cy="38" r="21" fill="var(--paper)"/>
      <circle cx="43" cy="38" r="16" fill="var(--icon)"/>
      <circle cx="43" cy="38" r="12" fill="var(--paper)"/>
      <circle cx="77" cy="16" r="4" fill="var(--paper)"/>
    </svg>
  </div>
  <div class="feature" style="left:200px;top:591px">
    <h3>Use My Images</h3>
    <p>Information Here</p>
  </div>

  <div class="icon" style="left:407px;top:563px;width:107px;height:90px">
    <svg viewBox="0 0 192 162" aria-hidden="true"><use href="#projector"/></svg>
  </div>
  <div class="feature" style="left:528px;top:591px">
    <h3>Use My Footage</h3>
    <p>Information Here</p>
  </div>

  <div class="icon" style="left:766px;top:576px;width:76px;height:86px">
    <svg viewBox="0 0 135 155" aria-hidden="true"><use href="#note"/></svg>
  </div>
  <div class="feature" style="left:853px;top:591px">
    <h3>Use My Background<br>Music</h3>
    <p class="em">Information Here</p>
  </div>
</main>
</body>
</html>
```